Quorivel Stationery

New startup called Quorivel (Zen + Intelligence) will primarily operate in the sustainable / responsible investment space. It will inform investors on optimising their investments as well as advise businesses on becoming better investment prospects.
The Zen is represents "low stress", calmness, quiet confidence. The intelligence refers to analytics, informed decisions, reliable, consistent.

The responsible / sustainable business space is one that balances financial success with progressing society and protecting nature. It understands that society needs a healthy natural environment to survive and financial success in the long term depends on a smooth functioning social context.

Beyond these elements it is desirable for the design to communicate integrity, trust, partner, collaboration, innovation, growth.

Please note: separate contest (#752143) for business card design
Updates

Project Deadline Extended
Reason: The design of these artefacts should probably align with the business card being designed in parallel running project 752143.

Target Market(s)

Medium sized businesses
Wealth optimising and ethical / responsible investors

Industry/Entity Type

Environment

Font styles to use
Other font styles liked:
• Rounded as on logo and back of business card

Requirements
Must have
• Must use attached logo
Templates:
- Letterhead and continuation (footers welcomed) (Word, A4, editable text)
- Comp slip
- Envelopes (DL)
- Notepad
- Email signature (Outlook)
- Report cover & continuation pages (Word, A4, editable text)
- Presentation pack (PowerPoint)

```html
<!DOCTYPE html>
<html lang="en">
<head>
<meta charset="utf-8">
<title>Quorivel Stationery</title>
<link rel="stylesheet" href="https://fonts.googleapis.com/css2?family=Cinzel:wght@400&family=Open+Sans:wght@400;600;700&display=swap">
<style>
  :root {
    --board: #e6e6e6;
    --paper: #ffffff;
    --orange: #f5861f;
    --label: #ef7f3a;
    --blue: #2f6cc0;
    --blue-light: #4a87d6;
    --green: #8dc63f;
    --ink: #3d3d3d;
    --ink-soft: #555555;
    --charcoal: #2f2f2f;
    --cover-dark: #1d1f20;
    --cover-mid: #6b6b6b;
  }
  * { box-sizing: border-box; margin: 0; padding: 0; }
  html, body { width: 1200px; height: 700px; overflow: hidden; }
  body { background: var(--board); font-family: "Open Sans", Arial, sans-serif; color: var(--ink); position: relative; }

  .board-label {
    position: absolute; font-family: "Cinzel", Georgia, serif; font-weight: 400;
    color: var(--label); font-size: 27px; letter-spacing: 0.5px; white-space: nowrap;
    transform: translateX(-50%);
  }

  .sheet { position: absolute; background: var(--paper); overflow: hidden; box-shadow: 0 1px 3px rgba(0,0,0,0.12); }

  /* Plain footer band: solid orange with a thin blue rule above */
  .footer-band { position: absolute; left: 0; right: 0; bottom: 0; background: var(--orange); }
  .footer-band::before { content: ""; position: absolute; left: 0; right: 0; top: -5px; height: 2px; background: var(--blue); }
  .letterhead .footer-band { height: 14px; }
  .envelope .footer-band { height: 22px; }
  .envelope .footer-band::before { top: -8px; height: 3px; }
  .card-front .footer-band { height: 10px; }
  .card-front .footer-band::before { top: -4px; }

  .brand { display: flex; align-items: center; gap: 5px; white-space: nowrap; }
  .brand-dot { border-radius: 50%; background: var(--orange); flex: none; }
  .brand-name { font-family: "Open Sans", Arial, sans-serif; font-weight: 600; color: var(--ink); }

  /* Letterheads */
  .letterhead { top: 58px; width: 260px; height: 370px; }
  .letterhead-1 { left: 45px; }
  .letterhead-2 { left: 328px; }
  .letterhead .brand { position: absolute; }
  .letterhead-1 .brand { top: 20px; left: 50%; transform: translateX(-50%); }
  .letterhead-1 .brand-dot { width: 26px; height: 26px; }
  .letterhead-1 .brand-name { font-size: 12px; }
  .letterhead-2 .brand { top: 14px; left: 26px; flex-direction: column; gap: 2px; }
  .letterhead-2 .brand-dot { width: 26px; height: 26px; }
  .letterhead-2 .brand-name { font-size: 9px; }
  .letterhead .watermark {
    position: absolute; left: 80px; top: 118px; width: 120px; height: 120px;
    border-radius: 50%; background: rgba(120,120,150,0.13);
  }
  .letter-contacts { position: absolute; top: 20px; right: 16px; font-size: 5px; line-height: 8px; color: var(--ink-soft); text-align: right; }
  .letter-contacts li { list-style: none; display: flex; justify-content: flex-end; align-items: center; gap: 3px; }
  .icon { display: inline-block; width: 4px; height: 4px; border: 0.8px solid var(--green); border-radius: 1px; }
  .letter-body { position: absolute; left: 10px; right: 10px; top: 90px; font-size: 4.6px; line-height: 6.4px; color: var(--ink-soft); }
  .letter-body p { margin-bottom: 6px; }
  .signature { width: 26px; height: 11px; background: linear-gradient(90deg, rgba(70,60,120,0.35), rgba(70,60,120,0.15)); border-radius: 6px; display: inline-block; }
  .seal { width: 14px; height: 14px; border-radius: 50%; background: #cfe4ee; display: inline-block; margin-left: 4px; }
  .sign-row { display: flex; align-items: center; margin-top: 8px; }

  /* Covers */
  .cover { top: 60px; width: 260px; height: 367px; }
  .cover-1 { left: 614px; background: linear-gradient(90deg, var(--cover-dark), var(--cover-mid)); }
  .cover-2 { left: 895px; background: linear-gradient(90deg, var(--blue), var(--blue-light)); }
  .cover .brand { position: absolute; top: 41px; left: 50%; transform: translateX(-50%); }
  .cover .brand-dot { width: 24px; height: 24px; }
  .cover .brand-name { color: #ffffff; font-size: 12px; }
  .cover .halo { position: absolute; left: 110px; top: 222px; width: 190px; height: 190px; border-radius: 50%; background: rgba(255,255,255,0.13); }

  /* Envelope */
  .envelope { left: 45px; top: 447px; width: 438px; height: 200px; }
  .envelope .brand { position: absolute; top: 14px; right: 16px; flex-direction: column; gap: 3px; align-items: center; }
  .envelope .brand-dot { width: 40px; height: 40px; }
  .envelope .brand-name { font-size: 12px; }
  .envelope-address { position: absolute; top: 82px; right: 16px; font-family: "Cinzel", Georgia, serif; font-size: 8px; line-height: 10px; color: var(--ink); text-align: left; }

  /* Business card front */
  .card-front { left: 539px; top: 468px; width: 275px; height: 158px; background: var(--charcoal); }
  .card-front .brand { position: absolute; top: 14px; left: 14px; }
  .card-front .brand-dot { width: 30px; height: 30px; }
  .card-front .brand-name { color: #ffffff; font-size: 15px; }
  .card-person { position: absolute; top: 56px; right: 14px; text-align: right; color: #ffffff; font-size: 6px; line-height: 7.5px; }
  .card-person .person-name { color: var(--green); font-weight: 700; font-size: 7.5px; }
  .card-rule { position: absolute; top: 84px; left: 14px; right: 14px; height: 1px; background: rgba(255,255,255,0.55); }
  .card-address { position: absolute; top: 94px; left: 14px; color: #ffffff; font-size: 5.5px; line-height: 7px; }
  .card-contacts { position: absolute; top: 92px; right: 14px; color: #ffffff; font-size: 6px; line-height: 7.5px; text-align: right; }
  .card-contacts li { list-style: none; display: flex; justify-content: flex-end; align-items: center; gap: 3px; }

  /* Business card back */
  .card-back { left: 865px; top: 468px; width: 276px; height: 158px; }
  .header-band { position: absolute; top: 0; left: 0; right: 0; height: 16px; background: var(--orange); }
  .header-band::after { content: ""; position: absolute; left: 0; right: 0; bottom: -5px; height: 2px; background: var(--blue); }
  .values { position: absolute; top: 62px; left: 8px; font-size: 7px; line-height: 15.3px; font-weight: 600; color: var(--ink); }
  .values li { list-style: none; display: flex; align-items: center; gap: 7px; }
  .values .ring { width: 7px; height: 7px; border-radius: 50%; border: 1.5px solid var(--blue); border-right-color: var(--orange); border-bottom-color: var(--green); }
  .card-back .brand { position: absolute; top: 53px; right: 12px; flex-direction: column; gap: 5px; align-items: center; }
  .card-back .brand-dot { width: 70px; height: 70px; }
  .card-back .brand-name { font-size: 15px; }
</style>
</head>
<body>

  <div class="board-label" style="left:175px; top:20px;">Letterhead 1</div>
  <div class="board-label" style="left:462px; top:20px;">Letterhead 2</div>
  <div class="board-label" style="left:746px; top:20px;">Cover Letter.. 1</div>
  <div class="board-label" style="left:1026px; top:20px;">Cover Letter.. 2</div>
  <div class="board-label" style="left:241px; top:655px;">Envelop</div>
  <div class="board-label" style="left:680px; top:637px;">Card Front</div>
  <div class="board-label" style="left:990px; top:637px;">Card Back</div>

  <section class="sheet letterhead letterhead-1">
    <div class="brand"><span class="brand-dot"></span><span class="brand-name">quorivel</span></div>
    <div class="watermark"></div>
    <div class="letter-body">
      <p>Ana Porter<br>42 River Rd<br>Perth, Australia</p>
      <p>Dear Ana Porter,</p>
      <p>Thank you for meeting with us last week. We have reviewed your portfolio and prepared a short summary of options that balance steady returns with clear social and environmental value. Each option is set out with its expected risk, time frame and reporting plan, so you can compare them calmly.</p>
      <p>Our analysts looked at energy, water and supply chain data for every holding. Where a company scores well, we suggest keeping it. Where it lags, we explain what would need to change before it becomes a sound long term prospect.</p>
      <p>We would welcome a second meeting to go through the numbers together. Please let us know a time that suits you, and we will send the full report a few days beforehand.</p>
      <p>Yours sincerely,<br>Tom Keane</p>
      <div class="sign-row"><span class="signature" role="img" aria-label="Handwritten signature"></span><span class="seal"></span></div>
    </div>
    <div class="footer-band"></div>
  </section>

  <section class="sheet letterhead letterhead-2">
    <div class="brand"><span class="brand-dot"></span><span class="brand-name">quorivel</span></div>
    <ul class="letter-contacts">
      <li>+61 8 4410 2207 <span class="icon"></span></li>
      <li>+61 8 4410 2290 <span class="icon"></span></li>
      <li>info@quorivel.com <span class="icon"></span></li>
      <li>www.quorivel.com <span class="icon"></span></li>
    </ul>
    <div class="watermark"></div>
    <div class="letter-body">
      <p>Ana Porter<br>42 River Rd<br>Perth, Australia</p>
      <p>Dear Ana Porter,</p>
      <p>Thank you for meeting with us last week. We have reviewed your portfolio and prepared a short summary of options that balance steady returns with clear social and environmental value. Each option is set out with its expected risk, time frame and reporting plan, so you can compare them calmly.</p>
      <p>Our analysts looked at energy, water and supply chain data for every holding. Where a company scores well, we suggest keeping it. Where it lags, we explain what would need to change before it becomes a sound long term prospect.</p>
      <p>We would welcome a second meeting to go through the numbers together. Please let us know a time that suits you, and we will send the full report a few days beforehand.</p>
      <p>Yours sincerely,<br>Tom Keane</p>
      <div class="sign-row"><span class="signature" role="img" aria-label="Handwritten signature"></span><span class="seal"></span></div>
    </div>
    <div class="footer-band"></div>
  </section>

  <section class="sheet cover cover-1">
    <div class="brand"><span class="brand-dot"></span><span class="brand-name">quorivel</span></div>
    <div class="halo"></div>
  </section>
  <section class="sheet cover cover-2">
    <div class="brand"><span class="brand-dot"></span><span class="brand-name">quorivel</span></div>
    <div class="halo"></div>
  </section>

  <section class="sheet envelope">
    <div class="brand"><span class="brand-dot"></span><span class="brand-name">quorivel</span></div>
    <p class="envelope-address">Here your company or<br>home address</p>
    <div class="footer-band"></div>
  </section>

  <section class="sheet card-front">
    <div class="brand"><span class="brand-dot"></span><span class="brand-name">quorivel</span></div>
    <div class="card-person">
      <div class="person-name">Mara Ellison</div>
      <div>B. Com (Hons), M. Fin</div>
      <div>Founder &amp; CEO</div>
    </div>
    <div class="card-rule"></div>
    <p class="card-address">Here your company or<br>home address</p>
    <ul class="card-contacts">
      <li>+61 8 4410 2207 <span class="icon"></span></li>
      <li>+61 8 4410 2290 <span class="icon"></span></li>
      <li>info@quorivel.com <span class="icon"></span></li>
      <li>www.quorivel.com <span class="icon"></span></li>
    </ul>
    <div class="footer-band"></div>
  </section>

  <section class="sheet card-back">
    <div class="header-band"></div>
    <ul class="values">
      <li><span class="ring"></span>communicate integrity</li>
      <li><span class="ring"></span>trust</li>
      <li><span class="ring"></span>partner</li>
      <li><span class="ring"></span>collaboration</li>
      <li><span class="ring"></span>innovation</li>
      <li><span class="ring"></span>growth</li>
    </ul>
    <div class="brand"><span class="brand-dot"></span><span class="brand-name">quorivel</span></div>
  </section>

</body>
</html>
```